Creative Wedding invitation with a roadmap needs a designer

Dear,

we two are from germany and are going to marry in our hometown croatia.
our guests will come from germany and some of them are locals.

We want to make a creative wedding invitation and for orientation to have the guests a small roadmap with our cellphone number on it and the 4 spots where everything will happen and a small timetable (programm)

The cardboard should be white with a silver or chrome effect color cut
The plasticcard should be silver or silver glitter on the front names + date on the backside a roadmap where the guests can see where the spots will be.

We attached you a sketch of our idea.

Basically its about a White DIN B6 Card with an extra envelope, centered on the Cardboard with a gluespot and a plastic card.

Thank you so much!

Mariella & Dominik
Updates

Target Market(s)

Wedding invitation

Industry/Entity Type

Wedding

Font styles to use
Serif
Decorative
Script

Requirements
Must have
• The cardboard should be white with a silver or chrome effect color cut
• The plasticcard should be silver or silver glitter on the front names + date on the backside a roadmap
Nice to have
• Translucent elements
• Colors: White, Silver, Glitter, Translucent
• Hologram with our the date or M&D

```html
<!DOCTYPE html>
<html lang="en">
<head>
<meta charset="utf-8">
<title>Mariella &amp; Dominik – Wedding Invitation</title>
<link rel="stylesheet" href="https://fonts.googleapis.com/css2?family=Allura&family=Quicksand:wght@400&display=swap">
<style>
  :root {
    --page-bg: #f2f2f0;
    --card-white: #ffffff;
    --ink: #2b1a14;
    --ink-soft: #4a3a34;
    --silver-light: #ececee;
    --silver-mid: #bfc0c4;
    --silver-deep: #8d8e93;
    --chrome-shine: #fafafa;
  }
  * { box-sizing: border-box; margin: 0; padding: 0; }
  html, body {
    width: 973px;
    height: 1200px;
    overflow: hidden;
    background: var(--page-bg);
  }
  .invitation {
    position: absolute;
    left: 126px;
    top: 50px;
    width: 720px;
    height: 1100px;
  }
  .glitter-frame {
    position: absolute;
    inset: 0;
    background:
      repeating-linear-gradient(45deg, rgba(255,255,255,0.35) 0 2px, rgba(0,0,0,0) 2px 5px),
      repeating-linear-gradient(-45deg, rgba(120,120,126,0.25) 0 1px, rgba(0,0,0,0) 1px 4px),
      linear-gradient(135deg, var(--silver-light), var(--silver-mid) 30%, var(--chrome-shine) 50%, var(--silver-deep) 72%, var(--silver-light));
  }
  .card-face {
    position: absolute;
    inset: 28px;
    background: var(--card-white);
  }
  .tagline {
    position: absolute;
    top: 112px;
    left: 0;
    right: 0;
    text-align: center;
    font-family: "Quicksand", sans-serif;
    font-size: 20px;
    line-height: 28px;
    letter-spacing: 1px;
    color: var(--ink-soft);
  }
  .glitter-splash {
    position: absolute;
    left: 103px;
    top: 256px;
    width: 520px;
    height: 500px;
    border-radius: 48% 52% 45% 55% / 50% 46% 54% 50%;
    background:
      radial-gradient(ellipse at 45% 50%, rgba(141,142,147,0.75) 0%, rgba(191,192,196,0.6) 40%, rgba(220,220,224,0.3) 62%, rgba(255,255,255,0) 72%);
  }
  .couple-names {
    position: absolute;
    left: 40px;
    right: 20px;
    top: 332px;
    font-family: "Allura", cursive;
    font-weight: 400;
    font-size: 138px;
    line-height: 156px;
    color: var(--ink);
  }
  .couple-names span { display: block; white-space: nowrap; }
  .couple-names .first-line { padding-left: 20px; }
  .event-details {
    position: absolute;
    top: 875px;
    left: 0;
    right: 0;
    text-align: center;
    font-family: "Quicksand", sans-serif;
    font-size: 22px;
    line-height: 32px;
    letter-spacing: 1px;
    color: var(--ink-soft);
  }
</style>
</head>
<body>
  <main class="invitation">
    <div class="glitter-frame" role="img" aria-label="Silver glitter border around the card"></div>
    <section class="card-face">
      <p class="tagline">Lorem ipsum dolor sit amet,<br>consectetur adipiscing elit</p>
      <div class="glitter-splash" role="img" aria-label="Scattered silver glitter splash behind the names"></div>
      <h1 class="couple-names">
        <span class="first-line">Mariella</span>
        <span class="second-line">&amp; Dominik</span>
      </h1>
      <p class="event-details">30.07.2017<br>address<br>telephone: +491702348815</p>
    </section>
  </main>
</body>
</html>
```